BRIARWOOD LOUNGE FRIDAY MAY 3

Flyer design for bar/nightclub event. Trying to keep a general theme with their flyers (see below) but would like to add some neon or some pop to it.

TEXT:

Briarwood Bar & Lounge Presents

LANTERN NIGHTS
GRAND OPENING EVENT

PURE HOUSE MUSIC W/

VORTEX
MARCO TELLEN
BRANDT & DJ WOBNIX

21+
9PM-130AM
712 K AVENUE DAVIS CA

Target Market(s)

House/dance music crowd.

Industry/Entity Type

Night Club

Font styles to use
Sans Serif

Colors
9bcb3c
fbee3d
ffffff

Requirements
Must have
• Large DJ names
Nice to have
• General theme of the attached flyers. Neon colors that stick with the theme. Anything else that looks cool will be considered

```html
<!DOCTYPE html>
<html lang="en">
<head>
<meta charset="utf-8">
<title>Briarwood Lounge – Lantern Nights</title>
<link rel="stylesheet" href="https://fonts.googleapis.com/css2?family=Roboto+Condensed:ital,wght@0,300;0,700;1,700&family=Josefin+Sans:wght@400;600&display=swap">
<style>
  :root {
    --page-bg: #d9d9d9;
    --flyer-top: #2e2306;
    --flyer-mid: #1c3a0c;
    --flyer-low: #05340f;
    --flyer-edge: #1a1a14;
    --brand-panel: #3d2f25;
    --brand-cream: #e8dfc6;
    --brand-gold: #e3ae2a;
    --white: #ffffff;
    --lime: #9bcb3c;
    --yellow: #fbee3d;
    --gold-a: #f2a84a;
    --gold-b: #f4d77a;
    --gold-c: #c9a06a;
  }
  * { box-sizing: border-box; margin: 0; padding: 0; }
  html, body { width: 1200px; height: 1200px; overflow: hidden; }
  body { background: var(--page-bg); position: relative; }

  .flyer {
    position: absolute; left: 259px; top: 78px; width: 683px; height: 995px;
    overflow: hidden;
    background: linear-gradient(180deg, var(--flyer-top) 0%, var(--flyer-top) 22%, var(--flyer-mid) 55%, var(--flyer-low) 78%, #0b1a0c 100%);
    border-top: 4px solid var(--flyer-edge);
    box-shadow: 0 8px 24px rgba(0,0,0,.25);
  }

  .smoke {
    position: absolute; left: 0; top: 300px; width: 683px; height: 420px;
    background:
      radial-gradient(ellipse 260px 90px at 420px 110px, rgba(200,150,60,.28), transparent 70%),
      radial-gradient(ellipse 180px 70px at 120px 60px, rgba(200,150,60,.18), transparent 70%),
      radial-gradient(ellipse 160px 160px at 560px 360px, rgba(110,170,110,.18), transparent 70%);
  }
  .crowd {
    position: absolute; left: 0; bottom: 0; width: 683px; height: 230px;
    background: linear-gradient(180deg, rgba(20,50,25,0) 0%, rgba(18,45,22,.85) 35%, #0e2410 100%);
  }
  .beams {
    position: absolute; left: 140px; top: 560px; width: 420px; height: 440px;
    background: radial-gradient(ellipse 120px 260px at 210px 300px, rgba(120,170,120,.18), transparent 70%);
  }

  .brand {
    position: absolute; left: 73px; top: 26px; width: 556px; height: 184px;
    background: var(--brand-panel);
    display: flex; align-items: center; justify-content: center; gap: 18px;
  }
  .brand-square { width: 34px; height: 34px; background: var(--brand-gold); }
  .brand-name {
    font-family: "Roboto Condensed", sans-serif; font-weight: 700;
    font-size: 50px; color: var(--brand-cream); letter-spacing: 1px;
  }

  .line { position: absolute; right: 25px; text-align: right; white-space: nowrap; }
  .presents {
    top: 234px; right: 82px;
    font-family: "Roboto Condensed", sans-serif; font-style: italic; font-weight: 700;
    font-size: 21px; color: var(--white);
  }
  .series {
    top: 282px;
    font-family: "Roboto Condensed", sans-serif; font-weight: 700;
    font-size: 46px; color: var(--white); letter-spacing: .5px;
  }
  .tagline {
    top: 364px;
    font-family: "Roboto Condensed", sans-serif; font-style: italic; font-weight: 700;
    font-size: 30px;
    background: linear-gradient(90deg, var(--lime) 0%, var(--lime) 45%, var(--yellow) 100%);
    -webkit-background-clip: text; background-clip: text; color: transparent;
  }
  .dj {
    font-family: "Josefin Sans", sans-serif; font-weight: 400;
    font-size: 52px; letter-spacing: 1px; line-height: 1;
    max-width: 620px;
    background: linear-gradient(90deg, var(--gold-a), var(--gold-b) 35%, var(--gold-c) 55%, var(--gold-b) 75%, var(--gold-a));
    -webkit-background-clip: text; background-clip: text; color: transparent;
  }
  .dj-1 { top: 448px; }
  .dj-2 { top: 528px; }
  .dj-3 { top: 606px; }

  .badge { position: absolute; left: 52px; top: 296px; width: 226px; height: 242px; }
  .badge-text {
    position: absolute; left: 52px; top: 336px; width: 218px;
    text-align: center;
    font-family: "Roboto Condensed", sans-serif; font-weight: 700;
    font-size: 37px; line-height: 44px;
    background: linear-gradient(90deg, var(--gold-a), var(--gold-b));
    -webkit-background-clip: text; background-clip: text; color: transparent;
  }

  .details {
    position: absolute; left: 120px; top: 714px; width: 545px; height: 80px;
    display: flex; align-items: flex-start;
    font-family: "Roboto Condensed", sans-serif; color: var(--gold-b);
  }
  .details .big { font-weight: 300; font-size: 46px; line-height: 56px; }
  .details .age { color: var(--gold-c); }
  .details .rule { width: 3px; height: 58px; background: var(--gold-a); margin: 4px 14px 0; }
  .details .address {
    font-weight: 700; font-size: 28px; line-height: 44px; text-align: center;
    color: var(--gold-b);
  }
</style>
</head>
<body>
  <main class="flyer">
    <div class="smoke" role="img" aria-label="Golden and green smoke wisps"></div>
    <div class="beams" role="img" aria-label="Stage light beams"></div>
    <div class="crowd" role="img" aria-label="Silhouetted dance crowd with raised hands"></div>

    <header class="brand">
      <span class="brand-square"></span>
      <span class="brand-name">BRIARWOOD LOUNGE</span>
    </header>

    <p class="line presents">Briarwood Bar &amp; Lounge Presents</p>
    <h1 class="line series">LANTERN NIGHTS</h1>
    <p class="line tagline">PURE HOUSE MUSIC WITH</p>

    <svg class="badge" viewBox="0 0 226 242" aria-hidden="true">
      <defs>
        <linearGradient id="hexFill" x1="1" y1="0" x2="0" y2="1">
          <stop offset="0" stop-color="#a9d63a"/>
          <stop offset="1" stop-color="#46bf4f"/>
        </linearGradient>
      </defs>
      <polygon points="113,6 220,66 220,182 113,242 6,182 6,66" fill="#d99ad0"/>
      <polygon points="109,2 214,60 214,176 109,236 4,176 4,60" fill="#ffffff"/>
      <polygon points="109,8 208,63 208,173 109,230 10,173 10,63" fill="url(#hexFill)"/>
    </svg>
    <p class="badge-text">GRAND<br>OPENING<br>EVENT</p>

    <h2 class="line dj dj-1">VORTEX</h2>
    <h2 class="line dj dj-2">MARCO TELLEN</h2>
    <h2 class="line dj dj-3">BRANDT &amp; DJ WOBNIX</h2>

    <section class="details">
      <span class="big age">21+</span>
      <span class="rule"></span>
      <span class="big">9PM-130AM</span>
      <span class="rule"></span>
      <span class="address">712 K AVENUE<br>DAVIS CA</span>
    </section>
  </main>
</body>
</html>
```